The Harbourline Aid Trust needs a graphic of their innovation approach

What we need?
- we have designed a new innovation approach (see attached). An innovation approach is the process one goes through in order to design and launch a new product or service.
- This new graphic will be used in meetings to help others understand what innovation is and how we do it. It will also be used in training sessions and be the starting point for innovation training materials we are creating
- We have created this draft graphic by copying and pasting new words over another charities innovation process
- We would like you to use your design magic and create our very own innovation process graphic. We would like it to be neat, simple, non fussy, easy to understand /read and in line with our brand colours
Attached:
1. PowerPoint:
- Slide 1: our innovation process
- Slide 2 explanation of process to bring it to life
- Slide 3&4: brand colours
- Slide 5: inspiration / examples of other processes we like the look of
2. Typeface brand guidelines
We can't wait to see what you come up with! Thank you :)
internal employees
Charity

```html
<!DOCTYPE html>
<html lang="en">
<head>
<meta charset="utf-8">
<title>Innovation Approach — The Harbourline Aid Trust</title>
<link rel="stylesheet" href="https://fonts.googleapis.com/css2?family=Roboto:wght@300;400;500;700&display=swap">
<style>
  :root {
    --header-bg: #f3f4f4;
    --discover-blue: #1c8bbf;
    --define-grey: #647b81;
    --deliver-green: #43a94b;
    --accent-red: #e2232b;
    --loop-white: #ffffff;
    --ink: #222426;
    --divider: #3a3f42;
  }
  html, body {
    margin: 0;
    padding: 0;
    width: 1200px;
    height: 850px;
    overflow: hidden;
    background: #ffffff;
  }
  .process-graphic {
    display: block;
    width: 1200px;
    height: 850px;
    font-family: "Roboto", Arial, sans-serif;
  }
  .phase-title {
    font-size: 19px;
    font-weight: 300;
    letter-spacing: 9px;
    fill: var(--ink);
    text-anchor: middle;
  }
  .loop { fill: none; stroke: var(--loop-white); stroke-width: 14; }
  .arrow-tip { fill: var(--loop-white); }
  .loop-label-light { fill: var(--loop-white); font-size: 15px; font-weight: 700; }
  .loop-label-dark { fill: var(--ink); font-size: 15px; font-weight: 700; }
  .connector { fill: none; stroke: var(--accent-red); stroke-width: 2; }
  .milestone-dot { fill: var(--accent-red); }
  .milestone-box { fill: var(--accent-red); stroke: #ffffff; stroke-width: 1; }
  .milestone-text { fill: #ffffff; font-size: 18px; font-weight: 700; text-anchor: middle; }
</style>
</head>
<body>
<svg class="process-graphic" viewBox="0 0 843 596" preserveAspectRatio="none" role="img" aria-label="Innovation approach: Discover, Define, Deliver">
  <defs>
    <path id="path-repeat-top" d="M316 161 A118 118 0 0 1 520 161"/>
    <path id="path-repeat-bottom" d="M307 495 A130 130 0 0 0 533 495"/>
    <path id="path-repeat-left" d="M99 453 A115 115 0 0 1 192 320"/>
    <path id="path-insight" d="M227 514 A82 82 0 0 0 289 461"/>
    <path id="path-conceive" d="M345 403 A80 80 0 0 1 393 355"/>
    <path id="path-test" d="M458 289 A80 80 0 0 0 493 247"/>
    <path id="path-delivery" d="M553 197 A82 82 0 0 1 644 144"/>
    <path id="path-improvement" d="M590 336 A118 118 0 0 0 746 204"/>
  </defs>

  <!-- Phase header -->
  <rect class="header-band" x="0" y="0" width="843" height="70" fill="var(--header-bg)"/>
  <text class="phase-title" x="160" y="42">DISCOVER</text>
  <text class="phase-title" x="423" y="42">DEFINE</text>
  <text class="phase-title" x="686" y="42">DELIVER</text>

  <!-- Phase columns -->
  <rect x="0" y="70" width="318" height="526" fill="var(--discover-blue)"/>
  <rect x="318" y="70" width="208" height="526" fill="var(--define-grey)"/>
  <rect x="526" y="70" width="317" height="526" fill="var(--deliver-green)"/>
  <line x1="318" y1="0" x2="318" y2="596" stroke="var(--divider)" stroke-width="1" stroke-dasharray="4 3"/>
  <line x1="526" y1="0" x2="526" y2="596" stroke="var(--divider)" stroke-width="1" stroke-dasharray="4 3"/>

  <!-- Loops -->
  <line class="loop" x1="54" y1="538" x2="212" y2="538"/>
  <circle class="loop" cx="212" cy="433" r="100"/>
  <circle class="loop" cx="420" cy="430" r="100"/>
  <circle class="loop" cx="418" cy="220" r="100"/>
  <circle class="loop" cx="630" cy="225" r="100"/>
  <path class="loop" d="M630 125 L790 120"/>
  <polygon class="arrow-tip" points="788,111 802,120 788,129"/>

  <!-- Direction markers -->
  <polygon class="arrow-tip" points="288,345 302,360 283,364"/>
  <polygon class="arrow-tip" points="128,352 118,368 139,366"/>
  <polygon class="arrow-tip" points="502,160 492,176 511,175"/>
  <polygon class="arrow-tip" points="338,160 350,145 354,164"/>
  <polygon class="arrow-tip" points="343,496 355,512 337,514"/>
  <polygon class="arrow-tip" points="506,490 518,476 522,494"/>
  <polygon class="arrow-tip" points="718,268 732,274 720,286"/>
  <polygon class="arrow-tip" points="550,290 566,292 556,306"/>

  <!-- Loop labels -->
  <text class="loop-label-dark"><textPath href="#path-repeat-top" startOffset="50%" text-anchor="middle">Repeat process</textPath></text>
  <text class="loop-label-dark"><textPath href="#path-repeat-bottom" startOffset="50%" text-anchor="middle">Repeat process</textPath></text>
  <text class="loop-label-dark"><textPath href="#path-repeat-left" startOffset="50%" text-anchor="middle">Repeat process</textPath></text>
  <text class="loop-label-light"><textPath href="#path-insight" startOffset="50%" text-anchor="middle">Insight</textPath></text>
  <text class="loop-label-light"><textPath href="#path-conceive" startOffset="50%" text-anchor="middle">Conceive</textPath></text>
  <text class="loop-label-light"><textPath href="#path-test" startOffset="50%" text-anchor="middle">Test</textPath></text>
  <text class="loop-label-light"><textPath href="#path-delivery" startOffset="50%" text-anchor="middle">Delivery Plan</textPath></text>
  <text class="loop-label-dark"><textPath href="#path-improvement" startOffset="50%" text-anchor="middle">Continuous improvement</textPath></text>

  <!-- Connectors -->
  <polyline class="connector" points="320,433 213,433 213,277"/>
  <polyline class="connector" points="421,330 421,473 554,473"/>
  <polyline class="connector" points="524,225 630,225 630,403"/>

  <!-- Milestones -->
  <circle class="milestone-dot" cx="320" cy="433" r="19"/>
  <circle class="milestone-dot" cx="421" cy="330" r="19"/>
  <circle class="milestone-dot" cx="524" cy="225" r="19"/>

  <rect class="milestone-box" x="137" y="212" width="153" height="65"/>
  <text class="milestone-text" x="213.5" y="239">Opportunity</text>
  <text class="milestone-text" x="213.5" y="263">Statement</text>

  <rect class="milestone-box" x="23" y="476" width="153" height="41"/>
  <text class="milestone-text" x="99.5" y="503">Challenge</text>

  <rect class="milestone-box" x="554" y="403" width="153" height="40"/>
  <text class="milestone-text" x="630.5" y="430">Solution</text>

  <rect class="milestone-box" x="554" y="455" width="153" height="40"/>
  <text class="milestone-text" x="630.5" y="482">Concepts</text>

  <rect class="milestone-box" x="668" y="142" width="152" height="40"/>
  <text class="milestone-text" x="744" y="169">Launch</text>
</svg>
</body>
</html>
```